Business Card Design Project

I am a property development company requiring a professional looking business card.
The name of the my company is KLV SUMMITRA. I have attached a couple of designs that I have created on my own, that can give you an idea of what I am after.
Above the wording KLV SUMMITRA, I have a orange arc above these words to signify the sun is begining to rise above the horizon.
I have a few designs; Middle Rays, Side Rays, Horizontals Rays which are OK, but I am looking for the better design.
The Rear design of the card is what I had came up with. If you have a better design, I am happy to see it.
The design of the card can follow what I have came up with, or it can be totally different. The fonts needs to be adjusted to another font that is more suitable.
The colours that I have used is what I think I would like to stick with. As I have mentioned, the orange arc is to signify the sun rising. If you have a better colour scheme, I would consider it.
Looking at dealing with first home buyers and proffesional people.
Business

```html
<!DOCTYPE html>
<html lang="en">
<head>
<meta charset="utf-8">
<title>KLV SUMMITRA – Business Card Options</title>
<link rel="stylesheet" href="https://fonts.googleapis.com/css2?family=Open+Sans:wght@400;600;700&family=Great+Vibes&display=swap">
<style>
  :root {
    --page: #ffffff;
    --card-edge: #8a8a8a;
    --ink: #231f20;
    --white: #ffffff;
    --red: #e2001a;
    --red-deep: #d90a22;
    --orange: #ec6a1a;
    --orange-mid: #f29a38;
    --orange-light: #f8cc92;
    --cream: #fdeec7;
    --cream-pale: #fff6dc;
    --cream-faint: #fffbec;
    --glow-core: #fffef2;
    --glow-warm: #ffe9a0;
    --glow-amber: #ffb52e;
    --night: #231f20;
    --script-gold: #e0781e;
  }
  * { margin: 0; padding: 0; box-sizing: border-box; }
  html, body {
    width: 1200px; height: 1152px; overflow: hidden;
    background: var(--page);
    font-family: "Open Sans", Arial, sans-serif;
  }
  .sheet { position: relative; width: 1200px; height: 1152px; }

  .card {
    position: absolute;
    width: 524px; height: 320px;
    border: 1px solid var(--card-edge);
    overflow: hidden;
  }
  .col-left  { left: 62px; }
  .col-right { left: 616px; }
  .row-1 { top: 64px; }
  .row-2 { top: 416px; }
  .row-3 { top: 767px; }

  .line {
    position: absolute; left: 0; right: 0;
    text-align: center; line-height: 1; white-space: nowrap;
  }
  .brand-name { font-size: 37px; font-weight: 400; letter-spacing: 0.5px; color: var(--ink); top: 60px; }
  .brand-line { font-size: 17px; font-weight: 400; color: var(--ink); top: 99px; }

  /* Front: horizontal bands */
  .front-bands {
    background: linear-gradient(to bottom,
      var(--white) 0 19.6%,
      var(--cream-faint) 19.6% 30%,
      var(--cream-pale) 30% 39.6%,
      var(--cream) 39.6% 50%,
      var(--orange-light) 50% 60%,
      var(--orange-mid) 60% 70%,
      var(--orange) 70% 80%,
      #e3341a 80% 90%,
      var(--red-deep) 90% 100%);
  }
  .front-bands .person-inline { font-size: 26px; font-weight: 700; color: var(--ink); top: 131px; }
  .front-bands .contact { font-size: 17px; font-weight: 700; color: var(--white); }
  .front-bands .c1 { top: 198px; }
  .front-bands .c2 { top: 231px; }
  .front-bands .c3 { top: 263px; }
  .front-bands .c4 { top: 294px; }

  /* Front: sun glow variants */
  .glow {
    position: absolute; inset: 0;
    background: radial-gradient(circle 200px at 50% 36%,
      var(--glow-core) 0%, var(--glow-core) 22%,
      var(--glow-warm) 42%, var(--glow-amber) 62%,
      var(--orange) 82%, var(--red) 100%), var(--red);
  }
  .glow-wide {
    background: radial-gradient(ellipse 300px 220px at 50% 36%,
      var(--glow-core) 0%, var(--glow-core) 20%,
      var(--glow-warm) 38%, var(--glow-amber) 55%,
      #f5451c 78%, var(--red) 100%), var(--red);
  }
  .person-name { font-size: 24px; font-weight: 700; color: var(--ink); top: 137px; }
  .person-role { font-size: 19px; font-weight: 700; color: var(--ink); top: 165px; }
  .glow-card .contact { font-size: 16px; font-weight: 700; color: var(--white); }
  .glow-card .c1 { top: 227px; }
  .glow-card .c2 { top: 247px; }
  .glow-card .c3 { top: 266px; }
  .glow-card .c4 { top: 286px; }

  .light-type .brand-name { font-weight: 600; }
  .light-type .person-name,
  .light-type .person-role,
  .light-type .contact { font-weight: 400; }

  /* Back */
  .back { background: var(--night); }
  .back .brand-name { color: var(--white); top: 129px; }
  .back .brand-line { color: var(--white); top: 172px; }
  .motto { font-size: 21px; font-weight: 700; color: var(--white); top: 205px; }
  .motto-script {
    font-family: "Great Vibes", cursive;
    font-size: 30px; font-weight: 400; color: var(--script-gold); top: 200px;
  }
</style>
</head>
<body>
<main class="sheet">

  <section class="card front-bands col-left row-1">
    <p class="line brand-name">KLV SUMMITRA</p>
    <p class="line brand-line">Property Developments</p>
    <p class="line person-inline">Marcus Lowe – Director</p>
    <p class="line contact c1">27 Ferris Lane Kirrawee NSW 2232 Australia</p>
    <p class="line contact c2">0412 308 594</p>
    <p class="line contact c3">marcus@klvsummitra.com.au</p>
    <p class="line contact c4">www.klvsummitra.com.au</p>
  </section>

  <section class="card glow-card col-right row-1">
    <div class="glow"></div>
    <p class="line brand-name">KLV SUMMITRA</p>
    <p class="line brand-line">Property Developments</p>
    <p class="line person-name">Marcus Lowe</p>
    <p class="line person-role">Director</p>
    <p class="line contact c1">27 Ferris Lane Kirrawee NSW 2232 Australia</p>
    <p class="line contact c2">0412 308 594</p>
    <p class="line contact c3">marcus@klvsummitra.com.au</p>
    <p class="line contact c4">www.klvsummitra.com.au</p>
  </section>

  <section class="card glow-card col-left row-2">
    <div class="glow glow-wide" role="img" aria-label="Sunburst of red and orange rays radiating from a bright centre"></div>
    <p class="line brand-name">KLV SUMMITRA</p>
    <p class="line brand-line">Property Developments</p>
    <p class="line person-name">Marcus Lowe</p>
    <p class="line person-role">Director</p>
    <p class="line contact c1">27 Ferris Lane Kirrawee NSW 2232 Australia</p>
    <p class="line contact c2">0412 308 594</p>
    <p class="line contact c3">marcus@klvsummitra.com.au</p>
    <p class="line contact c4">www.klvsummitra.com.au</p>
  </section>

  <section class="card glow-card light-type col-right row-2">
    <div class="glow glow-wide" role="img" aria-label="Sunburst of red and orange rays radiating from a bright centre"></div>
    <p class="line brand-name">KLV SUMMITRA</p>
    <p class="line brand-line">Property Developments</p>
    <p class="line person-name">Marcus Lowe</p>
    <p class="line person-role">Director</p>
    <p class="line contact c1">27 Ferris Lane Kirrawee NSW 2232 Australia</p>
    <p class="line contact c2">0412 308 594</p>
    <p class="line contact c3">marcus@klvsummitra.com.au</p>
    <p class="line contact c4">www.klvsummitra.com.au</p>
  </section>

  <section class="card back col-left row-3">
    <p class="line brand-name">KLV SUMMITRA</p>
    <p class="line brand-line">Property Developments</p>
    <p class="line motto">Build upon our Honesty &amp; Integrity</p>
  </section>

  <section class="card back col-right row-3">
    <p class="line brand-name">KLV SUMMITRA</p>
    <p class="line brand-line">Property Developments</p>
    <p class="line motto-script">Build upon our Honesty &amp; Integrity</p>
  </section>

</main>
</body>
</html>
```